KVL El Paso Juarez Leaders' Getaway at New Orleans

Leaders Getaway

Awesome weekend packed with business education, history, and food. Events to include:

* One with the owner of Willowmere Hotel and serial entrepreneur Dalton Fisk, Son of Vernon Fisk.

* Dine with Fellow KVLer Glen Staffield of Staffield's Family Restaurants. Hear the story of his family's success, divorce, failure, and how he elevated his family's business from the depths of failure to what it's today.

* Tour the Harbor Heritage Museum followed by an intimate session with WW2 vet and entrepreneur Martin Selwyn of Selwyn Vacuum Cleaners inside the Carrow Exchange Building that he purchased.

* Join us at Box Seats at the Gulf Coast Herons Game!

DATE & TIME
Starts Friday, November 2, 2018, 6:00 PM
Ends Sunday, November 4, 2018, 12:00 PM
VENUE
New Orleans
New Orleans, LA
United States
ATTENDANCE
KVL Members, KVL Spouses/Guests, KVL TEAL Members, KVL TEAL Spouses/Guests
DAY CHAIRS
Gordon & Linda Tavish

Invite 5x7 or 7x5 please

Target Market(s)

KVL El Paso Juarez Members

Industry/Entity Type

Non Profit

Font styles to use
Sans Serif
Script

Colors

Designer to choose colors to be used in the design.

Requirements
Must have
• Needs to be elegant
• Pictures
• Title
• Venue Info
• Date info
• Resources info
• Attendees info
• Logos
Nice to have
• graphics
Should not have
• Lantern Fest theme

```html
<!DOCTYPE html>
<html lang="en">
<head>
<meta charset="utf-8">
<title>KVL Sunland Valley Leaders' Getaway</title>
<link rel="stylesheet" href="https://fonts.googleapis.com/css2?family=Mulish:wght@400;600&family=Open+Sans:wght@400;700&family=Roboto+Condensed:wght@700&display=swap">
<style>
  :root {
    --gold: #d9a11c;
    --gold-light: #efc65a;
    --navy: #3b3f55;
    --ink: #555b6a;
    --paper: #ffffff;
    --backdrop: #e4e4e4;
    --haze: #eeeff1;
  }
  * { margin: 0; padding: 0; box-sizing: border-box; }
  html, body { width: 797px; height: 1200px; overflow: hidden; }
  body { background: var(--backdrop); position: relative; font-family: "Open Sans", sans-serif; }

  .invite {
    position: absolute;
    left: 18.5px; top: 69.5px;
    width: 439px; height: 613px;
    background: var(--paper);
    transform: scale(1.7312);
    transform-origin: 0 0;
    overflow: hidden;
  }
  .invite > * { position: absolute; }

  .backdrop-pattern { left: 0; top: 0; width: 439px; height: 360px; }

  .brand { left: 42px; top: 30px; display: flex; align-items: center; gap: 8px; }
  .brand-mark { width: 18px; height: 18px; background: var(--navy); }
  .brand-name { font-family: "Mulish", sans-serif; font-size: 25px; font-weight: 400; color: var(--navy); letter-spacing: 0.5px; line-height: 1; }
  .brand-divider { left: 154px; top: 22px; width: 1.2px; height: 50px; background: var(--gold); }
  .chapter { left: 171px; top: 35px; font-family: "Mulish", sans-serif; font-size: 20px; color: var(--navy); line-height: 1; white-space: nowrap; }

  .hero { left: 0; top: 0; width: 439px; height: 360px; }

  .highlights { left: 18px; top: 372px; width: 192px; list-style: none; }
  .highlights li {
    position: relative; padding-left: 18px;
    font-size: 8.4px; line-height: 11.5px; color: var(--ink);
    text-align: justify; margin-bottom: 12px;
  }
  .highlights li::before {
    content: ""; position: absolute; left: 2px; top: 3px;
    width: 6px; height: 6px; border-radius: 50%; background: #8a8e99;
  }
  .highlights li:nth-child(2) { margin-bottom: 13px; }

  .label { font-size: 11px; font-weight: 700; color: var(--gold); letter-spacing: 0.3px; line-height: 1; }
  .day-chairs { left: 33px; top: 572px; }
  .day-chairs p { font-size: 8.4px; color: var(--ink); margin-top: 3px; }

  .right { left: 222px; width: 200px; text-align: center; }
  .join { top: 369px; }
  .join .label { font-size: 10px; }
  .join p { font-size: 8px; line-height: 9.6px; color: var(--ink); text-transform: uppercase; margin-top: 3px; }

  .schedule { left: 224px; top: 411px; width: 197px; height: 64px; background: var(--gold); }
  .schedule::after {
    content: ""; position: absolute; inset: 2.5px;
    border: 1px solid var(--gold-light);
  }
  .schedule-split { position: absolute; left: 145px; top: 6px; width: 1px; height: 52px; background: var(--gold-light); }
  .schedule h3 { position: absolute; top: 9px; width: 100%; font-family: "Open Sans", sans-serif; font-size: 11px; font-weight: 700; color: var(--navy); line-height: 1; }
  .schedule .dates { position: absolute; left: 0; width: 145px; text-align: center; }
  .schedule .times { position: absolute; left: 145px; width: 52px; text-align: center; }
  .schedule ul { list-style: none; position: absolute; top: 25px; width: 100%; font-family: "Roboto Condensed", sans-serif; font-weight: 700; font-size: 7.8px; line-height: 13.5px; color: #fff; }
  .schedule sup { font-size: 5px; }

  .venue { left: 261px; top: 481px; width: 122px; height: 62px; text-align: center; }
  .venue-frame { position: absolute; left: 0; top: 0; width: 122px; height: 62px; }
  .venue .label { position: relative; padding-top: 2px; }
  .venue p { position: relative; font-size: 10.2px; line-height: 15px; color: var(--ink); margin-top: 2px; }

  .attendance { top: 559px; }
  .attendance p { font-size: 8.2px; line-height: 12px; color: var(--ink); margin-top: 3px; }
  .attendance .sep { color: var(--gold); padding: 0 2px; }

  .footer-band { left: 0; top: 609px; width: 439px; height: 4px; display: flex; }
  .footer-band span:first-child { width: 213px; background: var(--gold); }
  .footer-band span:last-child { flex: 1; background: var(--navy); }
</style>
</head>
<body>
  <article class="invite">
    <svg class="backdrop-pattern" viewBox="0 0 439 360" role="img" aria-label="Soft grey geometric background texture">
      <defs>
        <linearGradient id="haze" x1="0" y1="0" x2="0" y2="1">
          <stop offset="0" stop-color="#ffffff"/>
          <stop offset="0.45" stop-color="#eeeff1"/>
          <stop offset="1" stop-color="#ffffff"/>
        </linearGradient>
      </defs>
      <rect width="439" height="360" fill="url(#haze)"/>
    </svg>

    <div class="brand">
      <span class="brand-mark"></span>
      <span class="brand-name">KVL</span>
    </div>
    <div class="brand-divider"></div>
    <div class="chapter">Sunland Valley Chapter</div>

    <svg class="hero" viewBox="0 0 439 360">
      <defs>
        <linearGradient id="dusk" x1="0" y1="0" x2="0" y2="1">
          <stop offset="0" stop-color="#2d3140"/>
          <stop offset="0.3" stop-color="#8a4a26"/>
          <stop offset="0.42" stop-color="#c8722e"/>
          <stop offset="0.55" stop-color="#3a3a44"/>
          <stop offset="1" stop-color="#1b1c22"/>
        </linearGradient>
      </defs>
      <polygon points="218,81 398,346 41,346" fill="var(--gold)"/>
      <polygon points="218,108 369,331 68,331" fill="none" stroke="#ffffff" stroke-width="1.2"/>
      <polygon points="218,111 366,329 71,329" fill="url(#dusk)" role="img" aria-label="Night skyline of the New Orleans riverfront at sunset"/>
    </svg>

    <ul class="highlights">
      <li>One with the owner of Willowmere Hotel and serial entrepreneur Dalton Fisk, Son of Vernon Fisk.</li>
      <li>Dine with Fellow KVLer Glen Staffield of Staffield's Family Restaurants. Hear the story of his family's success, divorce, failure, and how he elevated his family's business from the depths of failure to what it's today.</li>
      <li>Tour the Harbor Heritage Museum followed by an intimate session with WW2 vet and entrepreneur Martin Selwyn of Selwyn Vacuum Cleaners inside the Carrow Exchange Building that he purchased.</li>
    </ul>

    <div class="day-chairs">
      <h2 class="label">DAY CHAIRS</h2>
      <p>Gordon &amp; Linda Tavish</p>
    </div>

    <div class="right join">
      <h2 class="label">JOIN US AT</h2>
      <p>Box seats at the<br>Gulf Coast Herons game!</p>
    </div>

    <section class="schedule">
      <span class="schedule-split"></span>
      <div class="dates">
        <h3>DATE</h3>
        <ul>
          <li>Starts-Friday, 2<sup>nd</sup> November, 2018</li>
          <li>Ends-Sunday, 4<sup>th</sup> November, 2018</li>
        </ul>
      </div>
      <div class="times">
        <h3>TIME</h3>
        <ul>
          <li>6:00 PM</li>
          <li>12:00 PM</li>
        </ul>
      </div>
    </section>

    <section class="venue">
      <svg class="venue-frame" viewBox="0 0 122 62">
        <g fill="none" stroke="var(--navy)" stroke-width="0.8">
          <polyline points="0.5,14 0.5,0.5 20,0.5"/>
          <polyline points="102,0.5 121.5,0.5 121.5,14"/>
          <polyline points="0.5,48 0.5,61.5 20,61.5"/>
          <polyline points="102,61.5 121.5,61.5 121.5,48"/>
        </g>
      </svg>
      <h2 class="label">VENUE</h2>
      <p>New Orleans<br>New Orleans, LA<br>United States</p>
    </section>

    <div class="right attendance">
      <h2 class="label">ATTENDANCE</h2>
      <p>KVL Members <span class="sep">|</span> KVL Spouses/Guests<br>KVL TEAL Members <span class="sep">|</span> KVL TEAL Spouses/Guests</p>
    </div>

    <div class="footer-band"><span></span><span></span></div>
  </article>
</body>
</html>
```